Newspaper AD in the Restaurant Section HOMECARE/Senior Living

Looking for an ad that is 6.425 inches wide and 5 inches tall to go into the newspaper weekly it will be in the restaurant section. We are a senior homecare company and we are looking to show clients that caregivers are able to assist them not only in personal care needs but also meal prep. We would like the design to have the feel of our existing ad or our newly launched website. It will be in the Savor section of the Pacific Morning Ledger which is not where we normally would advertise as a homecare agency so ad has to have some kind of feel for that section.
It should say somewhere maybe by contact info Call today for FREE Consultation.

Target Market(s)

Target market is Men/Women ages 35-105

Industry/Entity Type

Homecare and Senior Living

Font styles to use
Sans Serif

Colors
0054AA
0677BA
7BADD7
CADEEF
E8F1F8
FFF300
FFF600
FEFA6F
FFFEC7
FFFEE8
EB3D1F
EC4F4E
F09395
F8D3D4
FCEDEE

Requirements
Must have
• Logo, Contact info: Phone number (808) 555-0173, email address Info@brightmeadowcare.com and website www.Brightmeadowcare.com.
Nice to have
• Something that will be eye catching and to the point. Maybe a picture of a caregiver preparing a meal with an elderly person

```html
<!DOCTYPE html>
<html lang="en">
<head>
<meta charset="utf-8">
<title>Brightmeadow Homecare – Newspaper Ad</title>
<link rel="stylesheet" href="https://fonts.googleapis.com/css2?family=Lexend:wght@300;400;500;600;700&family=Source+Serif+4:opsz,wght@8..60,600;8..60,700&display=swap">
<style>
  :root {
    --teal-deep: #006e5f;
    --teal-bright: #00a99d;
    --salmon: #f4987e;
    --salmon-soft: #f7b7a4;
    --ink: #1e1e1e;
    --paper: #ffffff;
    --backdrop: #ececec;
    --dot-tint: #bfe3e2;
  }
  * { box-sizing: border-box; margin: 0; padding: 0; }
  html, body {
    width: 1200px; height: 1117px; overflow: hidden;
    background: var(--backdrop);
  }
  .canvas { position: relative; width: 1200px; height: 1117px; }
  .ad {
    position: absolute; left: 95px; top: 166px;
    width: 1009px; height: 785px;
    background: var(--paper); overflow: hidden;
    font-family: "Lexend", sans-serif; color: var(--ink);
  }
  .photo { position: absolute; top: 0; height: 272px; }
  .photo--sofa {
    left: 0; width: 505px;
    background: linear-gradient(120deg, #c9b98a 0%, #d8a874 30%, #3f7fc0 55%, #3fb3d6 70%, #b58b63 100%);
  }
  .photo--meal {
    left: 504px; width: 505px;
    background: linear-gradient(240deg, #e8e4c8 0%, #b8342f 35%, #9a7c6a 55%, #c98a5c 80%, #a06a3e 100%);
  }
  .top-shapes { position: absolute; left: 0; top: 0; width: 1009px; height: 300px; }
  .brand {
    position: absolute; left: 312px; top: 28px; width: 384px;
    text-align: center;
  }
  .brand__square {
    display: block; width: 72px; height: 72px; margin: 0 auto 14px;
    background: var(--salmon); border-radius: 10px;
  }
  .brand__name {
    font-family: "Source Serif 4", serif; font-weight: 600;
    color: var(--teal-deep); font-size: 46px; line-height: 48px;
    letter-spacing: -0.5px;
  }
  .headline {
    position: absolute; left: 36px; top: 318px; width: 500px;
    font-family: "Source Serif 4", serif; font-weight: 700;
    font-size: 70px; line-height: 68px; text-align: center;
    color: var(--teal-deep); letter-spacing: -1px;
  }
  .headline__accent { color: var(--teal-bright); }
  .dots { position: absolute; border-radius: 40px; }
  .dots--left {
    left: 8px; top: 480px; width: 160px; height: 205px;
    background: radial-gradient(ellipse at 20% 70%, var(--dot-tint) 0%, rgba(191,227,226,0.35) 45%, rgba(255,255,255,0) 75%);
  }
  .dots--right {
    left: 842px; top: 500px; width: 160px; height: 185px;
    background: radial-gradient(ellipse at 80% 60%, var(--dot-tint) 0%, rgba(191,227,226,0.35) 45%, rgba(255,255,255,0) 75%);
  }
  .services {
    position: absolute; left: 545px; top: 302px; width: 400px; height: 249px;
    border: 3px solid var(--salmon); border-radius: 22px; background: var(--paper);
  }
  .services__title {
    position: absolute; left: 28px; top: 24px; width: 338px; height: 42px;
    border-radius: 21px; background: var(--teal-deep); color: #fff;
    font-weight: 600; font-size: 27px; line-height: 42px; text-align: center;
  }
  .services__list {
    position: absolute; left: 27px; top: 82px; list-style: none;
  }
  .services__item {
    display: flex; align-items: center; height: 29px;
    font-weight: 500; font-size: 19.5px;
  }
  .services__tick { width: 19px; height: 19px; margin-right: 16px; flex: none; }
  .intro {
    position: absolute; left: 150px; top: 572px; width: 709px;
    text-align: center; font-weight: 300; font-size: 19px; line-height: 23px;
  }
  .bottom-shapes { position: absolute; left: 0; top: 620px; width: 1009px; height: 165px; }
  .cta {
    position: absolute; left: 167px; top: 648px; width: 676px;
    text-align: center; color: #fff; font-weight: 600; font-size: 31px;
  }
  .cta strong { font-weight: 700; }
  .contact {
    position: absolute; left: 0; top: 737px; width: 1009px;
    display: flex; justify-content: center; align-items: center;
    color: #fff; font-weight: 300; font-size: 19px;
  }
  .contact__item { display: flex; align-items: center; }
  .contact__icon { width: 20px; height: 20px; margin-right: 8px; }
  .contact__sep { margin: 0 12px; font-weight: 400; }
</style>
</head>
<body>
<div class="canvas">
  <div class="ad">
    <div class="photo photo--sofa" role="img" aria-label="Photo of a caregiver in blue scrubs chatting with a smiling client on a living room sofa"></div>
    <div class="photo photo--meal" role="img" aria-label="Photo of a caregiver in red scrubs serving a meal to an older couple at a dining table"></div>

    <svg class="top-shapes" viewBox="0 0 1009 300" aria-hidden="true">
      <circle cx="504" cy="192" r="192" fill="#ffffff"/>
      <rect x="312" y="190" width="384" height="110" fill="#ffffff"/>
      <path d="M0,205 Q180,255 330,268 L330,300 L0,300 Z" fill="#ffffff"/>
      <path d="M679,268 Q830,255 1009,205 L1009,300 L679,300 Z" fill="#ffffff"/>
      <path d="M0,195 Q180,252 325,262 L327,271 Q170,258 0,212 Z" fill="var(--teal-deep)"/>
      <path d="M0,226 Q160,262 270,267 L365,281 Q190,278 0,250 Z" fill="var(--salmon)"/>
      <path d="M1009,195 Q829,252 684,262 L682,271 Q839,258 1009,212 Z" fill="var(--teal-deep)"/>
      <path d="M1009,232 Q880,262 770,270 L835,281 Q930,272 1009,255 Z" fill="var(--teal-bright)"/>
    </svg>

    <div class="brand">
      <span class="brand__square"></span>
      <div class="brand__name">Brightmeadow<br>Homecare</div>
    </div>

    <div class="dots dots--left" role="img" aria-label="Soft teal halftone dot decoration"></div>
    <div class="dots dots--right" role="img" aria-label="Soft teal halftone dot decoration"></div>

    <h1 class="headline">Professional<br>Care In<br><span class="headline__accent">Your Home</span></h1>

    <section class="services">
      <h2 class="services__title">HOME SERVICES</h2>
      <ul class="services__list">
        <li class="services__item"><svg class="services__tick" viewBox="0 0 20 20"><circle cx="9" cy="11" r="7.5" fill="none" stroke="var(--teal-deep)" stroke-width="2"/><path d="M5.5,10.5 L9,14 L18,3" fill="none" stroke="var(--teal-deep)" stroke-width="2.2" stroke-linecap="round" stroke-linejoin="round"/></svg>Home Health Aides</li>
        <li class="services__item"><svg class="services__tick" viewBox="0 0 20 20"><circle cx="9" cy="11" r="7.5" fill="none" stroke="var(--teal-deep)" stroke-width="2"/><path d="M5.5,10.5 L9,14 L18,3" fill="none" stroke="var(--teal-deep)" stroke-width="2.2" stroke-linecap="round" stroke-linejoin="round"/></svg>Skilled Nursing (RN/LPN)</li>
        <li class="services__item"><svg class="services__tick" viewBox="0 0 20 20"><circle cx="9" cy="11" r="7.5" fill="none" stroke="var(--teal-deep)" stroke-width="2"/><path d="M5.5,10.5 L9,14 L18,3" fill="none" stroke="var(--teal-deep)" stroke-width="2.2" stroke-linecap="round" stroke-linejoin="round"/></svg>Bathing &amp; Meal Service</li>
        <li class="services__item"><svg class="services__tick" viewBox="0 0 20 20"><circle cx="9" cy="11" r="7.5" fill="none" stroke="var(--teal-deep)" stroke-width="2"/><path d="M5.5,10.5 L9,14 L18,3" fill="none" stroke="var(--teal-deep)" stroke-width="2.2" stroke-linecap="round" stroke-linejoin="round"/></svg>Medication Management</li>
        <li class="services__item"><svg class="services__tick" viewBox="0 0 20 20"><circle cx="9" cy="11" r="7.5" fill="none" stroke="var(--teal-deep)" stroke-width="2"/><path d="M5.5,10.5 L9,14 L18,3" fill="none" stroke="var(--teal-deep)" stroke-width="2.2" stroke-linecap="round" stroke-linejoin="round"/></svg>Services Available 24/7</li>
      </ul>
    </section>

    <p class="intro">Personal care services to meet your loved ones needs in<br>the comfort and safety of their own home</p>

    <svg class="bottom-shapes" viewBox="0 0 1009 165" aria-hidden="true">
      <path d="M167,95 Q190,22 240,20 L770,20 Q820,22 843,95 Z" fill="var(--salmon)"/>
      <path d="M0,58 Q504,125 1009,58 L1009,165 L0,165 Z" fill="var(--teal-deep)"/>
    </svg>

    <p class="cta">Call today for <strong>FREE</strong> Consultation.</p>

    <div class="contact">
      <span class="contact__item">
        <svg class="contact__icon" viewBox="0 0 20 20"><circle cx="10" cy="10" r="10" fill="#fff"/><path d="M6.5,5 L8.5,5 L9.3,7.6 L8.1,8.6 Q9.2,11 11.4,12 L12.4,10.8 L15,11.6 L15,13.6 Q14.6,15 13,15 Q5,14 5,6.8 Q5.2,5.2 6.5,5 Z" fill="var(--teal-deep)"/></svg>
        (808) 555-0173
      </span>
      <span class="contact__sep">|</span>
      <span class="contact__item">
        <svg class="contact__icon" viewBox="0 0 20 20"><circle cx="10" cy="10" r="10" fill="#fff"/><rect x="5" y="6.5" width="10" height="7" rx="1" fill="none" stroke="var(--teal-deep)" stroke-width="1.4"/><path d="M5.3,7 L10,10.8 L14.7,7" fill="none" stroke="var(--teal-deep)" stroke-width="1.4"/></svg>
        Info@brightmeadowcare.com
      </span>
      <span class="contact__sep">|</span>
      <span class="contact__item">
        <svg class="contact__icon" viewBox="0 0 20 20"><circle cx="10" cy="10" r="10" fill="#fff"/><circle cx="10" cy="10" r="5.5" fill="none" stroke="var(--teal-deep)" stroke-width="1.3"/><ellipse cx="10" cy="10" rx="2.3" ry="5.5" fill="none" stroke="var(--teal-deep)" stroke-width="1.1"/><path d="M4.5,10 L15.5,10" stroke="var(--teal-deep)" stroke-width="1.1"/></svg>
        www.Brightmeadowcare.com.
      </span>
    </div>
  </div>
</div>
</body>
</html>
```